Beauty Salon Industry - Web Design Project

zQuarta is a well-funded start up developing an Online Marketing Platform for small businesses in Europe.
We require a large number of high quality business web designs for our business website builder. Our business websites are seamlessly integrated into our Online Marketing systems and therefore it is important for designers to comply with our Design Guidelines.
This is our second contest and it will focus on the beauty salon industry. We will be running contents every 2-3 weeks for a new industry. Last month, we ran a contest for Builder website designs with 3 top prizes (plus £10 per variation) and we also paid out £25 per design for 20+ entries from designers who did not win the top prizes. So we encourage all entries!
We have included a wire frame this time to encourage you to be as creative as possible with your designs and layout while respecting the following guidelines:
1) You CAN change the layout as much as you like. If you think a vertical menu would look better, then use it. If you think the design would benefit from moving an element to a different location, then you can do that too.
2) You must include ALL the elements in the wire frame in your design.(e.g. latest 2 news entries, a testimonial, 1 gallery image, carousel etc...). Please make sure you have looked through the wire frame and know what is required. Entries that do not include all the elements will not qualify to win.
3) So remember, you CAN change the layout as much as you like but DO NOT remove any elements nor move them to a different page.
4) You may change the size and style of the carousel image. We would like to see as many variations of this as possible.
We are rewarding 3 prizes, and would like the winning designer to design the internal pages to the new design.
As always, if we think your designs could be incorporated into our system, but you do not win the competition, we will reward £25. Therefore, we encourage designers to submit as many designs as possible as we may award up to 25 designs.
Judging criteria : -
1) Visual Design
2) Layout must adhere to best practices and wireframe. If you decide to move elements around significantly please provide reason
3) Functional, informative and drives calls to action
Updates
As usual:
1st place = £350
2nd place = £250
3rd place = £150
Good luck!
Very happy with all the designs submitted so far, and will provide feedback ASAP.
We would like to see you try arranging the elements differently. So please try different navigation types and layouts.
Thanks
Morris
Prize funds for 1st place has been slightly increased.
Thanks
Morris
We have already had some amazing designs submitted. Thanks.
Remember to play with the layout of the elements and try designs with a carousel/slider that is in portrait not just in landscape.
Thanks everyone!
Morris
Hi everyone, we are really enjoying looking through the designs.
We have one NEW requirement. If you have used an image from http://www.frelik-example.com/ in your design, could you please replace it with another.
We are not associated with them.
Thank you.
I have just sent a poll around the office to vote on all the designs and hope to have the results soon.
Good luck and I hope to see all your great designs for our next project in a couple of weeks.
Morris
Hi everyone, we hope you have had a good holiday season. We will be rewarding the prizes very soon, hopefully today or tomorrow.
Thanks
Morris
We are currently going through all the designs that did not win our competition and will be contacting the designers of the designs we would like to use in our system, so please keep an eye on your inbox over the next few days.
Thank you
Morris
Target Market(s)
Beauty Salon Industry
Industry/Entity Type
Beauty Salon
Look and feel
Each slider illustrates characteristics of the customer's brand and the style your logo design should communicate.

```html
<!DOCTYPE html>
<html lang="en">
<head>
<meta charset="utf-8">
<title>Velvet Rush – Hair and Urban Spa</title>
<link href="https://fonts.googleapis.com/css2?family=PT+Sans:wght@400;700&family=PT+Sans+Narrow:wght@700&family=Arimo:wght@400&display=swap" rel="stylesheet">
<style>
:root{
  --green-dark:#3e620f;
  --green-link:#6c9a10;
  --nav-top:#72a22a;
  --nav-bottom:#3f6d0e;
  --red:#c2303e;
  --red-dark:#a8242f;
  --text:#222;
  --muted:#8a8a8a;
  --panel-a:#f6f6f6;
  --panel-b:#e2e2e2;
  --heading-grey:#444;
}
*{box-sizing:border-box;margin:0;padding:0}
html,body{width:1200px;height:1000px;overflow:hidden}
body{position:relative;background:#fff;font-family:"Arimo",Arial,sans-serif;color:var(--text)}
a{color:var(--green-link);text-decoration:none}
.abs{position:absolute}
.header{left:0;top:0;width:1200px;height:135px;background:linear-gradient(#e6e6e6,#fbfbfb 40%,#f4f4f4)}
.brand{left:128px;top:46px;font-family:"PT Sans",sans-serif;font-size:40px;color:var(--green-dark);letter-spacing:2px;line-height:1}
.brand-sub{left:226px;top:84px;font-family:"PT Sans",sans-serif;font-size:14px;color:#888}
.phone{right:145px;top:40px;font-family:"PT Sans",sans-serif;font-size:27px;color:var(--green-dark)}
.btn-red{background:linear-gradient(var(--red),var(--red-dark));color:#fff;font-family:"PT Sans Narrow",sans-serif;font-weight:700;text-align:center;border-radius:5px}
.book-now{left:940px;top:78px;width:116px;height:39px;line-height:39px;font-size:20px}
.nav{left:0;top:135px;width:1200px;height:51px;background:linear-gradient(var(--nav-top),var(--nav-bottom));display:flex;padding-left:135px;align-items:center}
.nav a{color:#fff;font-size:13px;margin-right:0}
.intro-title{left:131px;top:207px;font-family:"PT Sans",sans-serif;font-weight:700;font-size:20px;line-height:26px;color:var(--green-dark)}
.intro-text{left:131px;top:288px;width:210px;font-size:12.5px;line-height:23px}
.slider{left:351px;top:198px;width:498px;height:320px;background:linear-gradient(135deg,#dfe3e4,#c9cfc8 50%,#e6e8e6)}
.dots{left:547px;top:490px;display:flex;gap:4px}
.dots span{width:16px;height:16px;border-radius:50%;background:#fff}
.quote{left:362px;top:538px;width:480px;font-family:"PT Sans",sans-serif;font-weight:700;font-size:15px;line-height:25px;color:#333}
.quote-by{left:362px;top:592px;font-family:"PT Sans",sans-serif;font-weight:700;font-size:13px;color:var(--muted)}
.panel{background:linear-gradient(135deg,var(--panel-a),var(--panel-b));border-radius:5px}
.news{left:348px;top:620px;width:496px;height:132px}
.panel-h{font-family:"PT Sans Narrow",sans-serif;font-weight:700;font-size:18px;color:var(--heading-grey)}
.news-item{position:absolute;top:14px;font-size:12.5px;line-height:20px;color:#555}
.news-item .panel-h{margin-bottom:6px}
.more-news{left:354px;top:759px;font-size:13px}
.gallery-img{left:130px;top:628px;width:209px;height:122px;background:linear-gradient(90deg,#c9c9c9,#e8e4e2)}
.view-gallery{left:141px;top:760px;font-size:13px}
.gift{left:910px;top:208px}
.gift-price{left:868px;top:305px;font-family:"PT Sans",sans-serif;font-weight:700;font-size:28px}
.gift-text{left:868px;top:337px;font-family:"PT Sans",sans-serif;font-size:17px;line-height:23px;color:#777}
.book-appt{left:858px;top:392px;width:216px;height:49px;line-height:49px;font-size:22px;border-radius:4px}
.address{left:858px;top:447px;width:216px;height:110px;padding:6px 10px}
.rule{border-bottom:1px solid #d0d0d0;padding-bottom:2px;margin-bottom:4px}
.address p{font-size:13px;line-height:20px;padding-left:2px}
.hours{left:857px;top:562px;width:216px;height:190px;padding:6px 10px}
.hours table{margin:10px 0 0 10px;font-size:13px;border-collapse:collapse}
.hours td{padding:0 10px 3px 0;line-height:16px}
.brands{left:126px;top:805px;width:947px;height:107px;display:flex;align-items:center;justify-content:space-around;font-family:"PT Sans",sans-serif;font-size:24px;color:#222}
.footer{left:0;top:931px;width:1200px;height:69px;background:linear-gradient(#dcdcdc,#efefef)}
.footer-links{right:144px;top:949px;font-size:13px;color:#555}
.footer-links span{margin-left:24px}
</style>
</head>
<body>
<header class="abs header"></header>
<div class="abs brand">VELVET RUSH</div>
<div class="abs brand-sub">Hair and Urban Spa</div>
<div class="abs phone">020 7946 0185</div>
<a class="abs btn-red book-now" href="#">BOOK NOW</a>

<nav class="abs nav">
  <a href="#" style="width:74px">Home</a>
  <a href="#" style="width:89px">Services</a>
  <a href="#" style="width:72px">Gallery</a>
  <a href="#" style="width:111px">Testimonials</a>
  <a href="#" style="width:80px">News</a>
  <a href="#" style="width:92px">About us</a>
  <a href="#">Contact us</a>
</nav>

<h1 class="abs intro-title">LET OUR HAIR AND<br>BEAUTY SKILLS<br>BLOW VOU AWAY</h1>
<div class="abs intro-text">
  <p>Velvet Rush is a passionate creative team,dedicated to delivering a seconf to none,personal salon experience that will 'blow ' your mind</p>
  <p style="margin-top:23px">Where ultimate hairdressing comes hand-in-hand with style,glamour,fashion,innovation and skill to create an exquisite salon experience in the heart of london</p>
  <a href="#">more...</a>
</div>

<div class="abs slider" role="img" aria-label="Carousel photo of a model with styled hair and a green fur collar"></div>
<svg class="abs" style="left:362px;top:337px" width="16" height="32" viewBox="0 0 16 32"><path d="M15 1 1 16l14 15" fill="none" stroke="#fff" stroke-width="3"/></svg>
<svg class="abs" style="left:816px;top:337px" width="16" height="32" viewBox="0 0 16 32"><path d="M1 1l14 15L1 31" fill="none" stroke="#fff" stroke-width="3"/></svg>
<div class="abs dots"><span></span><span></span><span></span></div>

<p class="abs quote">My hairstylist, Marisa, was truly amazing. She listened to &nbsp;exactly what &nbsp;I wanted,but also told me exactly what</p>
<p class="abs quote-by">- Hanna Loweth</p>

<section class="abs panel news">
  <div class="news-item" style="left:14px;width:230px">
    <h2 class="panel-h">BOOK NOW FOR CHRISTMAS</h2>
    <p>Our saloon is usually very busy for the two weeks before Christmas, so please book early, call 020 7946 0185, or <a href="#">contact us</a></p>
  </div>
  <div class="news-item" style="left:276px;width:210px">
    <h2 class="panel-h">WANT TO BE A HAIR MODEL ?</h2>
    <p>We always need models for our portfolio If you want to become one please <a href="#">contact us</a></p>
  </div>
</section>
<a class="abs more-news" href="#">More News</a>

<div class="abs gallery-img" role="img" aria-label="Gallery photo of a stylist blow drying a client's hair"></div>
<a class="abs view-gallery" href="#">View Gallery</a>

<svg class="abs gift" width="110" height="95" viewBox="0 0 110 95" role="img" aria-label="Gift box">
  <rect x="17" y="30" width="76" height="62" fill="#f2f2f2" stroke="#ddd"/>
  <rect x="12" y="22" width="86" height="16" fill="#fafafa" stroke="#ddd"/>
  <rect x="48" y="22" width="14" height="70" fill="#d8101c"/>
  <path d="M55 22C40 0 18 8 30 20zM55 22C70 0 92 8 80 20z" fill="#e0141f"/>
</svg>
<div class="abs gift-price">£25</div>
<div class="abs gift-text">Complimentary gift for<br>first-time clients!</div>
<a class="abs btn-red book-appt" href="#">BOOK APPOINMENT NOW</a>

<section class="abs panel address">
  <h2 class="panel-h rule">VELVET ADDRESS</h2>
  <p>12 Larch Mews<br>London, W1x 3QP</p>
  <p style="margin-top:4px"><a href="#">View Map</a></p>
</section>

<section class="abs panel hours">
  <h2 class="panel-h rule" style="padding-left:4px">BUSINESS HOURS</h2>
  <table>
    <tr><td>Mon</td><td>9 am - 5 pm</td></tr>
    <tr><td>Tue</td><td>9 am - 5 pm</td></tr>
    <tr><td>Web</td><td>9 am - 5 pm</td></tr>
    <tr><td>Thu</td><td>9 am - 5 pm</td></tr>
    <tr><td>Fri</td><td>9 am - 5 pm</td></tr>
    <tr><td>Sat</td><td>9 am - 5 pm</td></tr>
  </table>
</section>

<section class="abs panel brands">
  <span>Lumera</span>
  <span>Corvane</span>
  <span>Brisa Vell</span>
  <span>Haldenmoor</span>
</section>

<footer class="abs footer"></footer>
<div class="abs footer-links">Managed by zquarta.com<span>Admin</span></div>
</body>
</html>
```